exclusive Speakeasy Bar Web design in New Jersey USA

We are opening a speakeasy in New Jersey USA soon. we are looking for a web designer to do our web site including the coding. we a looking for a 4 to 5 page web design. the site will be mostly static. home page, contact page, menu page and a link to a 3rd party site (most likely Qelmo) for reservations. we are looking for this designer to do our menu deign as well. we are looking for a quick turnaround 7-10 days. i am attaching some pictures for the designers to see the concept design and the actual current pictures with our logo as well. professionally taken pictures will be provided later on. our photographer will be taking the pictures in the next week.

Industry/Entity Type

Restaurant, Bar, Speakeasy

Coding

Coded - Design and coding required

Number of Pages Required

4 page

Requirements
Must have
• home page, contact page, menu page and a link to qelmo.com for reservations
Nice to have
• some videos

```html
<!DOCTYPE html>
<html lang="en">
<head>
<meta charset="utf-8">
<title>Lantern Room — Speakeasy</title>
<link href="https://fonts.googleapis.com/css2?family=Bebas+Neue&family=Oswald:wght@400;500;600&family=Roboto:wght@400;500&family=Great+Vibes&display=swap" rel="stylesheet">
<style>
:root{
  --bg:#000;
  --panel:#2a2725;
  --gold:#b89868;
  --gold-soft:#c9a97a;
  --white:#fff;
  --muted:#d8d2c8;
  --blue-text:#c6d2e2;
  --teal:#123a47;
  --line:#3a3a3a;
}
*{margin:0;padding:0;box-sizing:border-box}
html,body{width:1200px;height:4955px;overflow:hidden;background:var(--bg)}
body{position:relative;font-family:"Roboto",Arial,sans-serif;color:var(--white)}
.abs{position:absolute}
.photo{position:absolute}
.display{font-family:"Bebas Neue","Oswald",sans-serif;letter-spacing:.5px;line-height:.95}
.heading-gold{font-family:"Oswald",sans-serif;font-weight:500;color:var(--gold);text-transform:uppercase;font-size:30px;line-height:1.25}
.rule{position:absolute;height:3px;background:var(--gold)}
.body-text{font-size:13.5px;line-height:25px;color:var(--muted)}

/* header */
.site-header{position:absolute;left:0;top:0;width:1200px;height:85px;border-bottom:1px solid var(--line)}
.site-header .vline{position:absolute;top:0;width:1px;height:85px;background:var(--line)}
.nav{position:absolute;left:115px;top:32px;display:flex;gap:26px;font-family:"Oswald",sans-serif;font-size:13px;font-weight:500;letter-spacing:.5px}
.brand{position:absolute;left:553px;top:14px;width:94px;height:118px;border:2px solid var(--white);display:flex;align-items:center;justify-content:center;text-align:center;font-family:"Oswald",sans-serif;font-size:17px;line-height:1.1;background:var(--bg)}
.social{position:absolute;top:33px;display:flex;gap:18px;left:770px}
.social span{width:14px;height:14px;border-radius:50%;background:var(--white)}
.search{position:absolute;left:893px;top:31px}
.phone{position:absolute;left:978px;top:30px;font-family:"Oswald",sans-serif;font-size:17px;letter-spacing:1.5px}

/* hero */
.hero-title{left:550px;top:198px;font-size:76px}
.script-tag{position:absolute;left:905px;top:215px;width:70px;height:38px;border-top:2px solid var(--gold);border-bottom:2px solid var(--gold);font-family:"Great Vibes",cursive;color:var(--gold);font-size:28px;text-align:center;line-height:34px}
.info-row{position:absolute;left:715px;display:flex;gap:24px;font-family:"Oswald",sans-serif;font-size:12px;line-height:24px;letter-spacing:.5px}
.since-box{left:228px;top:775px;width:247px;height:93px;border-top:3px solid var(--gold);border-bottom:3px solid var(--gold);display:flex;align-items:center;justify-content:center;text-align:center;font-family:"Oswald",sans-serif;font-weight:500;color:var(--gold-soft);font-size:21px;line-height:26px;letter-spacing:1px}

/* menu */
.menu-item{position:absolute;left:618px;width:480px;height:70px}
.menu-item .cup{position:absolute;left:0;top:0;width:68px;height:68px;border-radius:50%}
.menu-item .name{position:absolute;left:88px;top:10px;right:0;display:flex;align-items:baseline;font-family:"Oswald",sans-serif;font-weight:500;font-size:17px}
.menu-item .dots{flex:1;border-bottom:2px dotted var(--white);margin:0 6px;transform:translateY(-4px)}
.menu-item .price{color:var(--gold-soft)}
.menu-item .old{color:#8a7a62;text-decoration:line-through;margin-right:10px}
.menu-item .desc{position:absolute;left:88px;top:42px;font-size:13px;color:#f2e0b5}
.menu-highlight{left:600px;top:1917px;width:513px;height:128px;border:2px solid var(--gold)}
.menu-highlight .tab{height:38px;background:var(--gold);font-family:"Oswald",sans-serif;font-size:12px;padding:12px 16px;letter-spacing:1px}

/* gallery */
.follow-btn{left:788px;top:3003px;width:249px;height:47px;border:2px solid var(--gold);display:flex;align-items:center;justify-content:center;gap:10px;font-family:"Oswald",sans-serif;font-size:15px;letter-spacing:2px;color:var(--gold-soft)}
.arrow{position:absolute;width:36px;height:36px;background:#e9e9e9;display:flex;align-items:center;justify-content:center}

/* contact */
.contact-card{left:87px;top:3622px;width:410px;height:593px;background:var(--panel)}
.field-label{position:absolute;font-size:13px;color:var(--white)}
.field-line{position:absolute;height:1px;background:#9a9a9a}
.send-btn{left:138px;top:4095px;width:125px;height:45px;background:var(--white);color:#000;font-family:"Oswald",sans-serif;font-size:13px;letter-spacing:2px;display:flex;align-items:center;justify-content:center}
.ghost-word{left:380px;top:3920px;font-size:300px;color:#1c1c1c;white-space:nowrap}

/* history */
.history{left:0;top:4275px;width:1200px;height:350px;background:var(--panel)}
.badge{left:528px;top:4368px;width:146px;height:146px;border-radius:50%;background:var(--teal);border:2px dashed #4d7584;display:flex;flex-direction:column;align-items:center;justify-content:center}

/* footer */
.footer-box{left:95px;top:4688px;width:1010px;height:112px;border:1px solid #555}
.footer-box .divider{position:absolute;top:0;width:1px;height:110px;background:#555}
.footer-cell{position:absolute;top:36px;display:flex;gap:22px;align-items:center;font-size:13px;line-height:22px}
.credit{left:0;top:4900px;width:1200px;text-align:center;font-family:"Oswald",sans-serif;font-size:14px;letter-spacing:1.5px}
</style>
</head>
<body>

<header class="site-header">
  <div class="vline" style="left:87px"></div>
  <div class="vline" style="left:497px"></div>
  <div class="vline" style="left:703px"></div>
  <div class="vline" style="left:960px"></div>
  <div class="vline" style="left:1150px"></div>
  <nav class="nav"><span>HOME</span><span>MENU ⌄</span><span>GALLERY ⌄</span><span>RESERVATIONS</span></nav>
  <div class="brand">LANTERN<br>ROOM</div>
  <div class="social" aria-label="Social links"><span></span><span></span><span></span></div>
  <svg class="search" width="16" height="16" viewBox="0 0 16 16"><circle cx="6.5" cy="6.5" r="5" stroke="#fff" stroke-width="2.2" fill="none"/><line x1="10" y1="10" x2="15" y2="15" stroke="#fff" stroke-width="2.4"/></svg>
  <div class="phone">234.555.0187</div>
</header>

<!-- hero -->
<div class="photo" role="img" aria-label="Orange spritz cocktails with citrus and bar tools" style="left:222px;top:90px;width:450px;height:560px;background:radial-gradient(circle at 45% 40%,#e07a22 0%,#8a3a0c 35%,#1a0d06 75%)"></div>
<h1 class="abs display hero-title">WHAT MAKES<br>HAPPY, AND UNIQUE</h1>
<div class="script-tag">us</div>
<div class="info-row" style="top:385px">
  <svg width="28" height="26" viewBox="0 0 28 26"><path d="M2 8l8-4 8 4 8-4v16l-8 4-8-4-8 4z" fill="#b89868"/></svg>
  <div>LOCATION BIRCH HOLLOW, MILLBROOK,<br>NEW JERSEY, USA</div>
</div>
<div class="info-row" style="top:452px">
  <svg width="28" height="26" viewBox="0 0 28 26"><circle cx="13" cy="12" r="10" stroke="#b89868" stroke-width="2.5" fill="none"/><path d="M13 6v6l4 3" stroke="#b89868" stroke-width="2.5" fill="none"/></svg>
  <div>SUN-THURS: 12PM-6PM<br>FRI-SAT: 12PM-8PM</div>
</div>
<div class="photo" role="img" aria-label="Bartender garnishing a cocktail with tweezers at the bar" style="left:517px;top:585px;width:596px;height:390px;background:linear-gradient(100deg,#08121c 0%,#1d3248 35%,#6b5a46 65%,#1a1410 100%)"></div>
<div class="abs since-box">SERVING TASTY<br>DRINKS SINCE 2023</div>

<!-- about -->
<div class="rule" style="left:525px;top:1112px;width:150px"></div>
<h2 class="abs heading-gold" style="left:617px;top:1128px;width:480px">The ultimate place to go when you're looking for a great time!</h2>
<p class="abs body-text" style="left:692px;top:1240px;width:420px">Exercitation photo booth stumptown tote bag street art, elit small batch freegan sed. Craft beer elit seitan exercitation, photo booth et 8-bit kale chips proident chillwave deep v laborum. Aliquip veniam delectus, desert town eiusmod moodboard in do umami readymade swag. Selfies smartphone crowdfunding, drinking vinegar jean vinegar stumptown yr pop-up artisan.</p>
<p class="abs body-text" style="left:692px;top:1427px;width:420px">Meh synth lager, tempor duis single-origin coffee ea next level ethnic fingerstache fanny pack nostrud. Photo booth anim 8-bit hella, cheap lager 3 wolf moon beard typeface.</p>
<div class="photo" role="img" aria-label="Bartender pouring a drink into a glass" style="left:113px;top:1157px;width:235px;height:363px;background:linear-gradient(180deg,#2a3640 0%,#c86a2a 60%,#241812 100%)"></div>
<div class="photo" role="img" aria-label="Martini glass on a bar board with snacks" style="left:265px;top:1395px;width:363px;height:253px;background:radial-gradient(circle at 50% 60%,#b07a3a 0%,#4a2a14 45%,#0e0906 90%)"></div>
<div class="abs" style="left:132px;top:1598px;width:300px;height:102px;overflow:hidden">
  <div class="display" style="font-size:84px">MAKES US<br>SERVE</div>
</div>

<!-- menu -->
<div class="abs heading-gold" style="left:283px;top:1722px;font-size:28px">Menus</div>
<div class="rule" style="left:378px;top:1740px;width:149px"></div>
<div class="photo" role="img" aria-label="Red holiday cocktails with festive lights" style="left:0;top:1825px;width:350px;height:460px;background:linear-gradient(90deg,#2a2c33 0%,#4a1a20 40%,#14161a 70%,#0a0a0a 100%)"></div>
<div class="abs" style="left:300px;top:1820px;width:110px;height:110px;border-radius:50%;border:2px dashed #2c2c2c"></div>
<div class="abs" style="left:402px;top:1832px;width:16px;height:16px;border-radius:50%;background:#2a2a2a"></div>
<div class="abs" style="left:385px;top:1955px;width:28px;height:28px;border-radius:50%;background:#2a2a2a"></div>

<div class="abs menu-highlight"><div class="tab">CLASSIC</div></div>
<div class="menu-item" style="top:1725px"><div class="cup" role="img" aria-label="Americano cup" style="background:radial-gradient(#3a2416 40%,#1d3a32 42%)"></div><div class="name">CAFE AMERICANO<span class="dots"></span><span class="old">$7</span><span class="price">$9</span></div><div class="desc">Espresso shots topped with hot water</div></div>
<div class="menu-item" style="top:1822px"><div class="cup" role="img" aria-label="Cappuccino cup" style="background:radial-gradient(#e8d2b4 40%,#1d3a32 42%)"></div><div class="name">CAPPUCCINO<span class="dots"></span><span class="price">$9</span></div><div class="desc">Dark espresso lies in wait under milk foam</div></div>
<div class="menu-item" style="top:1965px"><div class="cup" role="img" aria-label="Espresso cup" style="background:radial-gradient(#4a2a14 40%,#1d3a32 42%)"></div><div class="name">ESPRESSO<span class="dots"></span><span class="price">$5</span></div><div class="desc">Signature Espresso Roast with rich flavor</div></div>
<div class="menu-item" style="top:2068px"><div class="cup" role="img" aria-label="Caramel macchiato glass" style="background:radial-gradient(#c89a6a 40%,#1d3a32 42%)"></div><div class="name">CARAMEL MACCHIATO<span class="dots"></span><span class="price">$9</span></div><div class="desc">Freshly steamed milk with vanilla-flavored syrup</div></div>
<div class="menu-item" style="top:2165px"><div class="cup" role="img" aria-label="Caffe mocha with cream" style="background:radial-gradient(#f2ece4 40%,#1d3a32 42%)"></div><div class="name">CAFFE MOCHA<span class="dots"></span><span class="old">$6</span><span class="price">$7</span></div><div class="desc">Full-bodied espresso combined with mocha</div></div>

<!-- story -->
<div class="abs" style="left:700px;top:2378px;width:105px;height:137px;border:2px solid var(--white);display:flex;align-items:center;justify-content:center;text-align:center;font-family:'Oswald',sans-serif;font-size:18px;line-height:1.1">LANTERN<br>ROOM</div>
<div class="photo" role="img" aria-label="Lounge interior with mustard velvet chairs and painted mural" style="left:0;top:2487px;width:613px;height:406px;background:linear-gradient(180deg,#3a3e40 0%,#2c3032 45%,#b07a2a 70%,#5a4636 100%)"></div>
<div class="rule" style="left:525px;top:2561px;width:150px"></div>
<h2 class="abs heading-gold" style="left:692px;top:2545px">How we started</h2>
<p class="abs body-text" style="left:692px;top:2614px;width:420px;color:var(--blue-text)">Exercitation photo booth stumptown tote bag street art, elit small batch freegan sed. Craft beer elit seitan exercitation, photo booth et 8-bit kale chips proident chillwave deep v laborum. Aliquip veniam delectus, desert town eiusmod moodboard in do umami readymade swag. Selfies smartphone crowdfunding, drinking vinegar jean vinegar stumptown yr pop-up artisan.</p>
<p class="abs body-text" style="left:692px;top:2800px;width:420px;color:var(--blue-text)">Meh synth lager, tempor duis single-origin coffee ea next level ethnic fingerstache fanny pack nostrud. Photo booth anim 8-bit hella, cheap lager 3 wolf moon beard typeface.</p>

<!-- gallery -->
<div class="abs heading-gold" style="left:162px;top:3005px;font-size:28px">Gallery</div>
<div class="rule" style="left:275px;top:3024px;width:150px"></div>
<div class="abs follow-btn"><span style="width:14px;height:14px;border:2px solid var(--gold);border-radius:4px"></span>FOLLOW @LANTERNROOM</div>
<div class="photo" role="img" aria-label="Lounge chairs beside painted mural" style="left:0;top:3095px;width:175px;height:438px;background:linear-gradient(180deg,#3a3e40,#b07a2a 70%,#4a3a2e)"></div>
<div class="photo" role="img" aria-label="Back bar shelves stocked with bottles under arches" style="left:210px;top:3095px;width:780px;height:438px;background:linear-gradient(180deg,#2a241e 0%,#6a4a30 40%,#3a3a3a 75%,#1c1c1c 100%)"></div>
<div class="photo" role="img" aria-label="Bar counter with teal tiled front" style="left:1025px;top:3095px;width:175px;height:438px;background:linear-gradient(180deg,#4a3e34,#8a5a3a 50%,#1f5a5a 80%,#2a2a2a)"></div>
<div class="arrow" style="left:35px;top:3297px"><svg width="10" height="14"><path d="M8 1L2 7l6 6" stroke="#000" stroke-width="2" fill="none"/></svg></div>
<div class="arrow" style="left:1127px;top:3297px"><svg width="10" height="14"><path d="M2 1l6 6-6 6" stroke="#000" stroke-width="2" fill="none"/></svg></div>

<!-- contact -->
<div class="abs display ghost-word">CONTACT</div>
<div class="abs contact-card"></div>
<div class="abs" style="left:400px;top:3600px;width:185px;height:185px;border-radius:50%;border:2px dashed #2a2a2a"></div>
<div class="abs" style="left:592px;top:3592px;width:22px;height:22px;border-radius:50%;background:#2e2e2e"></div>
<div class="abs" style="left:578px;top:3735px;width:32px;height:32px;border-radius:50%;background:#2e2e2e"></div>
<div class="rule" style="left:63px;top:3690px;width:150px"></div>
<h2 class="abs heading-gold" style="left:230px;top:3668px;font-size:28px">Contact</h2>
<svg class="abs" style="left:138px;top:3748px" width="28" height="24" viewBox="0 0 28 26"><path d="M2 8l8-4 8 4 8-4v16l-8 4-8-4-8 4z" fill="#b89868"/></svg>
<div class="abs" style="left:188px;top:3745px;font-size:13px;line-height:25px">Location Birch Hollow,<br>NEW JERSEY, USA</div>
<svg class="abs" style="left:138px;top:3832px" width="24" height="24" viewBox="0 0 24 24"><path d="M5 2l4 1 2 5-3 2a12 12 0 006 6l2-3 5 2 1 4c0 2-2 3-4 3A18 18 0 012 6c0-2 1-4 3-4z" fill="#b89868"/></svg>
<div class="abs" style="left:188px;top:3835px;font-size:13px">234.555.0187</div>
<div class="field-label" style="left:138px;top:3898px">Name:</div>
<div class="field-line" style="left:138px;top:3943px;width:262px"></div>
<div class="field-label" style="left:138px;top:3990px">Subject:</div>
<div class="field-line" style="left:138px;top:4038px;width:262px"></div>
<div class="abs send-btn">SEND</div>

<!-- history -->
<div class="abs history"></div>
<div class="photo" role="img" aria-label="Illuminated back bar with bottle shelves" style="left:600px;top:4275px;width:600px;height:350px;background:linear-gradient(180deg,#2a241e,#7a5432 45%,#2a2a2a 85%)"></div>
<h2 class="abs display" style="left:78px;top:4338px;font-size:42px">HISTORY</h2>
<p class="abs" style="left:78px;top:4392px;width:340px;font-size:13px;line-height:25px">Craft beer elit seitan exercitation, photo booth et 8-bit kale chips proident chillwave deep v laborum. Aliquip veniam delectus, desert town eiusmod moodboard in do umami readymade swag.</p>
<div class="abs" role="img" aria-label="Owner signature" style="left:78px;top:4528px;width:220px;height:42px;background:linear-gradient(90deg,#3a3633,#4a4540,#3a3633)"></div>
<div class="abs badge"><span style="font-size:12px;color:#c6d2e2">since</span><span class="display" style="font-size:40px">2023</span></div>

<!-- footer -->
<div class="abs footer-box">
  <div class="divider" style="left:353px"></div>
  <div class="divider" style="left:757px"></div>
  <div class="footer-cell" style="left:35px">
    <svg width="46" height="40" viewBox="0 0 46 40"><path d="M4 14c0-6 8-10 19-10s19 4 19 10l-7 3-3-5H13l-3 5z" stroke="#b89868" stroke-width="2" fill="none"/><rect x="11" y="18" width="24" height="18" rx="3" stroke="#b89868" stroke-width="2" fill="none"/><circle cx="23" cy="27" r="5" stroke="#b89868" stroke-width="2" fill="none"/></svg>
    <div>Openning Hours<br>11.30AM – 2.30PM</div>
  </div>
  <div class="footer-cell" style="left:388px">
    <svg width="40" height="44" viewBox="0 0 40 44"><circle cx="20" cy="25" r="16" stroke="#b89868" stroke-width="2" fill="none"/><rect x="16" y="2" width="8" height="6" stroke="#b89868" stroke-width="2" fill="none"/><path d="M20 14v11l7 4" stroke="#b89868" stroke-width="2" fill="none"/></svg>
    <div>Location Birch Hollow, Millbrook<br>NEW JERSEY, USA</div>
  </div>
  <div class="social" aria-label="Social links" style="left:830px;top:48px"><span></span><span></span><span></span></div>
</div>
<div class="abs" style="left:0;top:4865px;width:1200px;height:1px;background:#333"></div>
<div class="abs credit">© 2023 LANTERN ROOM</div>
<svg class="abs" style="left:1163px;top:4905px" width="12" height="14"><path d="M6 13V2M1 6l5-5 5 5" stroke="#fff" stroke-width="1.5" fill="none"/></svg>

</body>
</html>
```